Loomvista: fashion design product software needs your help

Fashion design product software company requests your assistance in designing a complete stationary package around our new logo design. Our software assists fashion designers and apparel houses with efficient communication and streamlined production between each other and manufacturers throughout the entire project design life cycle.

The look should reflect clean, simple and modern design. Not too "techie." Must use the provided logo and colors (or variations on the chosen colors, i.e. percentages as needed).

Reference website: www.loomvista-example.com

Buzzwords: manufacturing, production, apparel design/ers, streamlined process, effective communication, business, production software.

Please try to tone down or make the colors more subtle with more simple design style, layout. No sewing  theme. Thank you.

Target Market(s)

fashion designers and apparel houses that use software to manage and track production process life cycle.

Industry/Entity Type

Communication

Requirements
Must have
• Use of the logo and colors-or variations of colors (attached)
Nice to have
• Playfulness but corporate: with a sense of practicality, economical, streamlined production. Embossing considered.
Should not have
• Please keep in mind economics both financially and economically. Save trees and money! We believe in tactile paper but not "fashion-y" or sparkly, over-the-top colors, effects or production.

```html
<!DOCTYPE html>
<html lang="en">
<head>
<meta charset="utf-8">
<title>Loomvista Letterhead</title>
<link rel="stylesheet" href="https://fonts.googleapis.com/css2?family=Varela+Round&display=swap">
<style>
  :root {
    --brown: #6b3320;
    --blue: #1db3e8;
    --paper: #ffffff;
  }
  html, body {
    margin: 0;
    padding: 0;
    overflow: hidden;
    background: var(--paper);
  }
  .letterhead {
    position: relative;
    width: 848px;
    height: 1200px;
    background: var(--paper);
    overflow: hidden;
    font-family: "Varela Round", Arial, sans-serif;
  }
  .brand {
    position: absolute;
    left: 46px;
    top: 78px;
    display: flex;
    align-items: center;
    gap: 14px;
  }
  .brand-name {
    font-size: 58px;
    line-height: 1;
    color: var(--brown);
    letter-spacing: -0.5px;
  }
  .brand-dot {
    width: 30px;
    height: 30px;
    border: 3px solid var(--blue);
    border-radius: 50%;
  }
  .contact {
    position: absolute;
    left: 185px;
    top: 250px;
    margin: 0;
    font-style: normal;
    font-size: 11.5px;
    line-height: 20px;
    color: var(--brown);
  }
  .punch-holes {
    position: absolute;
    left: 0;
    top: 0;
  }
</style>
</head>
<body>
<main class="letterhead">
  <header class="brand">
    <span class="brand-name">loomvista</span>
    <span class="brand-dot"></span>
  </header>

  <address class="contact">
    218 Weaver Street<br>
    Millbrook, NY 10990<br>
    555-014-2370<br>
    contact@loomvista-example.com
  </address>

  <svg class="punch-holes" width="848" height="1200" viewBox="0 0 848 1200" aria-hidden="true">
    <g fill="var(--paper)" stroke="var(--brown)" stroke-width="2">
      <circle cx="44" cy="238" r="7"/>
      <circle cx="44" cy="380" r="7"/>
      <circle cx="44" cy="523" r="7"/>
      <circle cx="44" cy="651" r="7"/>
      <circle cx="44" cy="792" r="7"/>
      <circle cx="44" cy="935" r="7"/>
      <circle cx="44" cy="1077" r="7"/>
    </g>
  </svg>
</main>
</body>
</html>
```